Flyer for Gathering L.I.T. - Evening of Glory!

We are producing a monthly Evening of Glory that supports local Christian Contemporary artists and raises money for charities. We are looking for a flyer design for our flyers, posters, and postcards (some mailed and some handed out). We want to create a modern and impressive flyer that will capture audiences.

Event details -
Tag: experience the night. praise the night.
A Evening of Glory you will not want to miss
Let's worship! Live band covering your favorite popular contemporary Christian music! All ages welcome!
Date: Wednesday, May 27th, 2015
7:00 pm to 8:15 pm
Location: The Harborlight Church
2750 S Maple Ridge Rd; Fort Lauderdale, FL 33871

Event is FREE!! Please bring a donation of gently used clothing items or new toiletry item.
Benefit for: The Hopeful Hands Mission

This month's debut artist: Celeste Varnham - local Christian Singer/Songwriter.

for more details, visit: www.gatheringgloryLIT.example
brought to you by: Margot Tellwell Music
___
Please see our website for style of what we are looking for. Also attached is a template design that I like and would love to see if we can do something like this.

Target Market(s)

all ages - young, older, modern, contemporary - youth

Industry/Entity Type

Artists

Colors
ec1f27
6b449b
ffffff

Requirements
Must have
• Cool design, bring a new "vibe" to Christian music -
• Black design
• worship photos like in the attached template ideas.

```html
<!DOCTYPE html>
<html lang="en">
<head>
<meta charset="utf-8">
<title>Gathering L.I.T. - Evening of Glory</title>
<link rel="stylesheet" href="https://fonts.googleapis.com/css2?family=Cinzel:wght@600&family=Roboto:wght@300;400;700&family=Roboto+Condensed:wght@300;400;700&display=swap">
<style>
  :root {
    --ink: #050505;
    --paper: #ffffff;
    --gold: #e3b22a;
    --purple: #6b449b;
    --purple-soft: #8a63c2;
    --red: #ec1f27;
    --muted: #d8d8d8;
  }
  * { box-sizing: border-box; margin: 0; padding: 0; }
  html, body { width: 796px; height: 1200px; overflow: hidden; background: var(--ink); }
  .poster {
    position: relative; width: 796px; height: 1200px; overflow: hidden;
    background: radial-gradient(ellipse at 50% 18%, #2a2a2a 0%, #0d0d0d 45%, var(--ink) 75%);
    color: var(--paper);
    font-family: "Roboto", Arial, sans-serif;
    text-align: center;
  }
  .tagline {
    position: absolute; top: 42px; left: 0; right: 0;
    font-weight: 400; font-size: 27px; line-height: 1.2;
    letter-spacing: 1px; text-transform: uppercase;
  }
  .title {
    position: absolute; top: 170px; left: 0; right: 0;
    font-family: "Roboto Condensed", Arial, sans-serif; font-weight: 700;
    color: var(--gold); line-height: 1;
  }
  .title-word { display: block; font-size: 122px; letter-spacing: 3px; }
  .title-tag { display: block; font-size: 58px; letter-spacing: 4px; margin-top: 8px; padding-left: 260px; }
  .event-name {
    position: absolute; top: 402px; left: 0; right: 0;
    font-family: "Cinzel", Georgia, serif; font-weight: 600;
    font-size: 36px; letter-spacing: 11px; color: var(--purple-soft);
  }
  .intro {
    position: absolute; top: 464px; left: 80px; right: 80px;
    font-size: 13.5px; line-height: 1.6; color: var(--muted);
  }
  .venue {
    position: absolute; top: 560px; left: 88px; right: 60px;
    display: flex; align-items: center; gap: 14px; text-align: left;
  }
  .venue-lead {
    font-family: "Roboto Condensed", Arial, sans-serif; font-weight: 300;
    font-size: 56px; line-height: 1; white-space: nowrap;
  }
  .venue-name { font-family: "Roboto Condensed", Arial, sans-serif; font-size: 22px; line-height: 1.1; text-transform: uppercase; }
  .venue-address { font-size: 12px; color: var(--muted); }
  .venue-date { font-family: "Roboto Condensed", Arial, sans-serif; font-weight: 700; font-size: 24px; line-height: 1.2; }
  .time {
    position: absolute; top: 620px; left: 0; right: 0;
    font-family: "Roboto Condensed", Arial, sans-serif; font-size: 52px; font-weight: 400;
  }
  .time b { font-weight: 700; }
  .ages {
    position: absolute; top: 686px; left: 0; right: 0;
    font-family: "Roboto Condensed", Arial, sans-serif; font-weight: 700; font-size: 24px;
  }
  .debut {
    position: absolute; top: 720px; left: 0; right: 0;
    font-family: "Roboto Condensed", Arial, sans-serif; font-size: 15px; color: var(--muted);
  }
  .debut b { color: var(--paper); font-weight: 700; }
  .stage-photo {
    position: absolute; top: 748px; left: 0; right: 0; height: 330px;
    background:
      radial-gradient(ellipse at 50% 10%, rgba(255,235,200,0.35) 0%, transparent 40%),
      radial-gradient(ellipse at 20% 55%, rgba(120,90,160,0.35) 0%, transparent 30%),
      radial-gradient(ellipse at 82% 55%, rgba(150,90,200,0.45) 0%, transparent 30%),
      radial-gradient(ellipse at 50% 70%, rgba(200,150,90,0.35) 0%, transparent 50%),
      linear-gradient(180deg, #0a0806 0%, #2b1d12 50%, #120c08 100%);
  }
  .footer {
    position: absolute; left: 0; right: 0; bottom: 0; height: 122px;
    background: var(--ink); display: flex; align-items: center; justify-content: space-between;
    gap: 12px; padding: 0 20px 0 22px; text-align: left;
  }
  .footer-info {
    font-family: "Roboto Condensed", Arial, sans-serif;
    font-size: 13px; line-height: 1.45; color: var(--paper); white-space: nowrap;
  }
  .partners { display: flex; gap: 8px; align-items: center; flex-shrink: 0; }
  .partner {
    width: 48px; height: 36px; background: var(--paper); color: #222;
    font-family: "Roboto Condensed", Arial, sans-serif; font-size: 8px; line-height: 1.1;
    display: flex; align-items: center; justify-content: center; text-align: center; padding: 2px;
  }
  .partner-host {
    width: 62px; height: 62px; border: 3px solid var(--purple); background: #1a1a1a; color: var(--paper);
    font-family: "Roboto Condensed", Arial, sans-serif; font-size: 9px; line-height: 1.15;
    display: flex; align-items: center; justify-content: center; text-align: center; padding: 3px;
  }
</style>
</head>
<body>
  <main class="poster">
    <p class="tagline">Experience the night<br>Praise the night</p>

    <h1 class="title">
      <span class="title-word">GATHERING</span>
      <span class="title-tag">L.I.T.</span>
    </h1>

    <h2 class="event-name">EVENING OF GLORY</h2>

    <p class="intro">An Evening of Glory you will not want to miss. Let's worship! Live band covering your favorite popular contemporary Christian music! A wonderful night that is sure to move your entire soul. Come worship with us! Features live music covering some of your favorite Christian Singers like Riverstone, Kindred Fire, Elias Corbin, Wren Adler, Hollow Pines, Jonah Ashby, and many, many more!</p>

    <section class="venue">
      <span class="venue-lead">SEE IT LIVE AT</span>
      <div class="venue-details">
        <div class="venue-name">The Harborlight Church</div>
        <div class="venue-address">2750 S Maple Ridge Rd; Fort Lauderdale, FL 33871</div>
        <div class="venue-date">Wednesday, May 27th, 2015</div>
      </div>
    </section>

    <p class="time"><b>7:00</b> pm to <b>8:15</b> pm</p>
    <p class="ages">All ages welcome!</p>
    <p class="debut">This month's debut artist: <b>Celeste Varnham</b> - local Christian Singer/Songwriter</p>

    <div class="stage-photo" role="img" aria-label="Worship stage with spotlights beaming down, flanked by two screens showing the live band"></div>

    <footer class="footer">
      <div class="footer-info">
        Event is FREE!! Please bring a donation of gently used clothing items or new toiletry item.<br>
        Benefit for: The Hopeful Hands Mission<br>
        for more details, visit: www.gatheringgloryLIT.example<br>
        brought to you by: Margot Tellwell Music
      </div>
      <div class="partners">
        <div class="partner">Harborlight Church</div>
        <div class="partner">Hopeful Hands</div>
        <div class="partner">Seaside County</div>
        <div class="partner-host">Margot Tellwell Music</div>
      </div>
    </footer>
  </main>
</body>
</html>
```